Full cover (front, back and side of the book). 28 cm x 20 cm total (High 20 cm, width 13, side 2 cm) Front cover: Title of the author on top, centered (Mathieu Clavreux) Title: Counting the rivers Subtitle: Sailing keeper coastal Bottom and centered: attached logo (Vorelma Editions) in white, and edited eventualy. Side: From left to right: Editor logo (only "Vorelma" word, without the "Editions" word, title and author name Back cover: Left text column ) Bottom: space available for the bar coded price and 2 or 3 lines of text Right text column (approx 6.5 cm wide) Bottom of the right colum, center of the right column: same attached logo (Vorelma Editions) in white, and edited eventualy, with www.vorelma.example below the logo. Left Lateral margin of the back cover, this book should be almost 1 cm)
Colors
Designer to choose colors to be used in the design.

```html
<!DOCTYPE html>
<html lang="en">
<head>
<meta charset="utf-8">
<title>Counting the rivers — full cover</title>
<link rel="stylesheet" href="https://fonts.googleapis.com/css2?family=Bebas+Neue&family=Oswald:wght@500;700&family=Arimo:wght@400&display=swap">
<style>
  :root {
    --page: #ffffff;
    --spine: #2f5878;
    --sky-top: #50667f;
    --sky-mid: #6f8299;
    --lagoon: #3fb3bd;
    --lagoon-light: #7fcfc7;
    --sand: #aec3ac;
    --back-wash: #557592;
    --back-wash-low: #6d8ea4;
    --ink: #0d1a26;
    --white: #ffffff;
    --title-top: #e6f3fb;
    --title-low: #8cc6ea;
    --logo-tint: #fbe9f3;
  }
  * { box-sizing: border-box; margin: 0; padding: 0; }
  html, body { width: 1200px; height: 1200px; overflow: hidden; background: var(--page); }

  .cover { position: absolute; left: 0; top: 145px; width: 1200px; height: 886px; }

  .back-cover {
    position: absolute; left: 0; top: 0; width: 558px; height: 886px;
    background:
      linear-gradient(180deg, rgba(80,110,140,.55) 0%, rgba(80,110,140,0) 40%),
      linear-gradient(180deg, var(--back-wash) 0%, #5d7f9c 45%, #4f7791 62%, var(--back-wash-low) 100%);
  }
  .spine {
    position: absolute; left: 558px; top: 0; width: 80px; height: 886px;
    background: var(--spine);
  }
  .front-cover {
    position: absolute; left: 638px; top: 0; width: 562px; height: 886px;
    background:
      linear-gradient(180deg, var(--sky-top) 0%, var(--sky-mid) 30%, #7f93a6 42%, #3c5e58 47%, var(--lagoon) 52%, #35b4c1 64%, var(--lagoon-light) 80%, var(--sand) 100%);
  }

  .body-copy {
    position: absolute; top: 87px;
    font-family: "Arimo", Arial, sans-serif; font-size: 17px; line-height: 28px; color: var(--ink);
  }
  .body-copy--left { left: 34px; width: 195px; }
  .body-copy--right { left: 253px; width: 280px; text-align: justify; hyphens: auto; }
  .isbn { margin-top: 28px; }

  .price-box { position: absolute; left: 34px; top: 729px; width: 187px; height: 114px; background: var(--white); }

  .imprint {
    position: absolute; left: 0; width: 100%; text-align: center;
    font-family: "Oswald", sans-serif; font-weight: 700; text-transform: uppercase; color: var(--white);
  }
  .imprint--back { left: 253px; width: 280px; top: 770px; font-size: 30px; line-height: 34px; }
  .imprint--front { top: 808px; font-size: 34px; line-height: 38px; color: var(--logo-tint); }
  .imprint__name { display: block; }
  .site-url {
    position: absolute; left: 253px; width: 280px; top: 820px; text-align: center;
    font-family: "Arimo", Arial, sans-serif; font-size: 21px; color: var(--white);
  }

  .spine-title, .spine-author {
    position: absolute; left: 40px; white-space: nowrap; color: var(--white);
    transform-origin: 0 0; transform: rotate(90deg) translateY(-50%);
  }
  .spine-title { top: 35px; font-family: "Bebas Neue", sans-serif; font-size: 44px; line-height: 1; }
  .spine-author { top: 559px; font-family: "Oswald", sans-serif; font-weight: 500; font-size: 17px; letter-spacing: 9px; }
  .spine-imprint {
    position: absolute; left: 0; width: 80px; top: 840px; text-align: center;
    font-family: "Oswald", sans-serif; font-weight: 700; font-size: 13px; color: var(--white); text-transform: uppercase;
  }

  .front-author {
    position: absolute; left: 0; width: 100%; top: 30px; text-align: center;
    font-family: "Oswald", sans-serif; font-weight: 500; font-size: 30px; letter-spacing: 15px; color: var(--white);
    text-indent: 15px;
  }
  .front-title {
    position: absolute; left: 0; width: 100%; top: 100px; text-align: center;
    font-family: "Bebas Neue", sans-serif; font-size: 124px; line-height: 96px;
    background: linear-gradient(180deg, var(--title-top) 0%, var(--title-low) 48%, var(--title-top) 52%, var(--title-low) 100%);
    -webkit-background-clip: text; background-clip: text; color: transparent;
  }
  .front-subtitle {
    position: absolute; left: 0; width: 100%; top: 318px; text-align: center;
    font-family: "Bebas Neue", sans-serif; font-size: 40px; color: var(--white);
  }
</style>
</head>
<body>
<main class="cover">
  <section class="back-cover" role="img" aria-label="Faded aerial photograph of a tropical lagoon under cloudy sky">
    <p class="body-copy body-copy--left">Full cover (front, back and side of the book). 28 cm x 20 cm total (High 20 cm, width 13, side 2 cm) Front cover: Title of the author on top, centered (Mathieu Clavreux) Title: Counting the rivers Subtitle: Sailing keeper coastal Bottom and centered: attached logo (Vorelma Editions) in white, and edited eventualy. Side: From left to nd edited eventualy, with niobhoivwbnoinvas ncjd jiohsiowbd nionsv
      <span class="isbn" style="display:block">ISBN 46892470291<br>NIOEVIOMVPW</span></p>
    <p class="body-copy body-copy--right">Full cover (front, back and side of the book). 28 cm x 20 cm total (High 20 cm, width 13, side 2 cm) Front cover: Title of the author on top, centered (Mathieu Clavreux) Title: Counting the rivers Subtitle: Sailing keeper coastal Bottom and centered: attached logo (Vorelma Editions) in white, and edited eventualy. Side: From left to right: Editor logo (only "Vorelma" word, without the "Editions" word, title and author name Back cover: Left text column ) Bottom: space available for the bar coded price and 2 or 3 lines of text Right text column (approx 6.5 cm wide) Bottom of the right colum, center of the right column: same attached logo (Vorelma Editions) in white, and edited eventualy, with</p>
    <div class="price-box"></div>
    <div class="imprint imprint--back"><span class="imprint__name">Vorelma Editions</span></div>
    <p class="site-url">www.vorelma.example</p>
  </section>

  <section class="spine">
    <h2 class="spine-title">COUNTING THE RIVERS</h2>
    <p class="spine-author">MATHIEU CLAVREUX</p>
    <p class="spine-imprint">Vorelma</p>
  </section>

  <section class="front-cover" role="img" aria-label="Aerial photograph of a small aircraft flying over a turquoise lagoon with a mountainous island">
    <p class="front-author">MATHIEU CLAVREUX</p>
    <h1 class="front-title">COUNTING<br>THE RIVERS</h1>
    <p class="front-subtitle">SAILING KEEPER COASTAL</p>
    <div class="imprint imprint--front"><span class="imprint__name">Vorelma Editions</span></div>
  </section>
</main>
</body>
</html>
```